immediate money for financial solutions

We need a Clean yet, eye catching, Business Card denoting a professional financial/tech firm. The front should have our logo and the notion that we are money lenders that get business loans quickly & easily. Maybe shade the colors of our logo. We are opened, but not committed to an unusual shaped card. The Back Should have our Business Contact Info & logo found on our website's front page: KORVANTINC.COM

Financial

```html
<!DOCTYPE html>
<html lang="en">
<head>
<meta charset="utf-8">
<title>Korvant Inc Business Card</title>
<link rel="stylesheet" href="https://fonts.googleapis.com/css2?family=Lato:wght@400;700&display=swap">
<style>
  :root {
    --page-bg: #dfe7f6;
    --card-bg: #ffffff;
    --brand-green: #2e9f49;
    --brand-teal: #1a937a;
    --band-green: #35a548;
    --text-light: #ffffff;
  }
  * { margin: 0; padding: 0; box-sizing: border-box; }
  html, body {
    width: 1200px;
    height: 965px;
    overflow: hidden;
    background: var(--page-bg);
    font-family: "Lato", Arial, sans-serif;
  }
  .canvas { position: relative; width: 1200px; height: 965px; }
  .card {
    position: absolute;
    left: 285px;
    width: 630px;
    background: var(--card-bg);
    overflow: hidden;
  }
  .card-front { top: 80px; height: 360px; }
  .card-back { top: 524px; height: 361px; }

  .brand-name {
    position: absolute;
    color: var(--brand-green);
    font-weight: 400;
    font-size: 38px;
    letter-spacing: 1px;
    white-space: nowrap;
  }
  .card-front .brand-name { left: 0; right: 0; top: 168px; text-align: center; }
  .card-back .brand-name { left: 42px; top: 76px; }

  .wave { position: absolute; left: 0; top: 0; width: 630px; height: 361px; }

  .holder { position: absolute; left: 40px; top: 252px; color: var(--text-light); }
  .holder-name { font-size: 23px; line-height: 28px; }
  .holder-title { font-size: 16px; line-height: 20px; }

  .contact-list {
    position: absolute;
    left: 360px;
    top: 256px;
    list-style: none;
    color: var(--text-light);
    font-size: 16px;
  }
  .contact-list li { display: flex; align-items: center; height: 21px; }
  .contact-list svg { width: 18px; height: 14px; margin-right: 12px; flex: none; }
</style>
</head>
<body>
<div class="canvas">
  <section class="card card-front">
    <div class="brand-name">KORVANT INC</div>
  </section>

  <section class="card card-back">
    <div class="brand-name">KORVANT INC</div>

    <svg class="wave" viewBox="0 0 630 361" aria-hidden="true">
      <path d="M0,176 C150,215 320,240 470,196 C545,173 600,170 630,182 L630,361 L0,361 Z" fill="var(--brand-teal)"/>
      <path d="M0,188 C130,222 270,236 420,220 C520,210 590,222 630,248" fill="none" stroke="#ffffff" stroke-width="4"/>
      <path d="M0,192 C130,226 270,240 420,224 C520,214 590,226 630,252 L630,361 L0,361 Z" fill="var(--band-green)"/>
    </svg>

    <div class="holder">
      <div class="holder-name">Daniel Reyes</div>
      <div class="holder-title">President/Lender</div>
    </div>

    <ul class="contact-list">
      <li>
        <svg viewBox="0 0 18 14" aria-hidden="true"><path d="M2,5 C2,2 16,2 16,5 L13,6 L12,4 L6,4 L5,6 Z M5,7 L13,7 L15,13 L3,13 Z" fill="#fff"/></svg>
        917.555.0143
      </li>
      <li>
        <svg viewBox="0 0 18 14" aria-hidden="true"><rect x="1" y="1" width="16" height="12" fill="none" stroke="#fff" stroke-width="1.6"/><path d="M1,1 L9,8 L17,1" fill="none" stroke="#fff" stroke-width="1.6"/></svg>
        Daniel@korvantinc.com
      </li>
      <li>
        <svg viewBox="0 0 18 14" aria-hidden="true"><rect x="1" y="1" width="16" height="12" fill="none" stroke="#fff" stroke-width="1.6"/><path d="M1,1 L9,8 L17,1" fill="none" stroke="#fff" stroke-width="1.6"/></svg>
        ATMinfo@korvantinc.com
      </li>
      <li>
        <svg viewBox="0 0 18 14" aria-hidden="true"><circle cx="9" cy="7" r="6" fill="none" stroke="#fff" stroke-width="1.4"/><ellipse cx="9" cy="7" rx="2.6" ry="6" fill="none" stroke="#fff" stroke-width="1.2"/><path d="M3,7 L15,7" stroke="#fff" stroke-width="1.2"/></svg>
        www.KORVANTINC.COM
      </li>
    </ul>
  </section>
</div>
</body>
</html>
```